business card with 2 locations on 1 card

I need a modern looking business card that I would use at 2 different locations. Possibly 1 location on 1 side and other location on other side. One should be able to distinguish the 2 locations immediately before having to read the address or description on card. You can take a look at my website to see what I'm drawn to. The logo is brand new that I just purchased on Craft Hive. I want to emphasize family.
Updates

Let's not use the yellow and blue colors. Added Thursday, August 31, 2017

Target Market(s)

women and children

Industry/Entity Type

Health And Wellness

Contact Information for Business Card

Business name: Willow Brook Chiropractic & Acupuncture
My name: Lorin Daske
Job title: DC, MAOM, LAc (CA), CNS

Location 1
Address: 4817 Marlowe Blvd, Suite B-100, Frisco, TX 75034
Phone: (469) 555-0182
Fax: (972) 555-0137

Location 2
Address: 1936 Belvane Road, Suite 100, Plano, TX 75075
Phone: (469) 555-0169
Fax: (972) 555-0137

Email: drlorindaske@mailnest.example
Website: www.drlorindaske.example

Font styles to use
Serif
Sans Serif

Colors

Designer to choose colors to be used in the design.

Requirements
Must have
• distinction between 2 locations.
Nice to have
• Colors preference below is there. But I like to see what you come up with too!

```html
<!DOCTYPE html>
<html lang="en">
<head>
<meta charset="utf-8">
<title>Willow Brook Chiropractic &amp; Acupuncture — Locations Card</title>
<link href="https://fonts.googleapis.com/css2?family=Montserrat:wght@600&display=swap" rel="stylesheet">
<style>
  :root {
    --teal-deep: #1b7868;
    --teal-bar: #2a7f6b;
    --teal-text: #27796a;
    --paper: #ffffff;
  }
  * { margin: 0; padding: 0; box-sizing: border-box; }
  html, body { width: 1200px; height: 804px; overflow: hidden; background: var(--paper); }
  .card {
    position: relative;
    width: 1200px;
    height: 804px;
    background: var(--paper);
    font-family: "Montserrat", sans-serif;
    font-weight: 600;
    color: var(--teal-text);
    overflow: hidden;
  }
  .side-band {
    position: absolute;
    left: 852px; top: 0;
    width: 348px; height: 804px;
    background: var(--teal-deep);
  }
  .location-tab {
    position: absolute;
    left: 0;
    width: 411px; height: 76px;
    background: var(--teal-bar);
    box-shadow: 2px 3px 5px rgba(0,0,0,0.18);
    color: var(--paper);
    font-size: 29px;
    letter-spacing: 0.16em;
    line-height: 76px;
    padding-left: 135px;
  }
  .tab-one { top: 77px; }
  .tab-two { top: 434px; }
  .details {
    position: absolute;
    left: 135px;
    font-size: 29px;
    letter-spacing: 0.16em;
    line-height: 33px;
    white-space: nowrap;
  }
  .details p { margin-bottom: 34px; }
  .details .address { margin-bottom: 33px; }
  .details-one { top: 166px; }
  .details-two { top: 524px; }
  .brand-seal {
    position: absolute;
    left: 683px; top: 230px;
    width: 336px; height: 336px;
  }
  .brand-name {
    font-family: "Montserrat", sans-serif;
    font-weight: 600;
    font-size: 30px;
    letter-spacing: 0.06em;
    fill: var(--teal-deep);
  }
</style>
</head>
<body>
  <main class="card">
    <div class="side-band"></div>

    <div class="location-tab tab-one">Location 1</div>
    <section class="details details-one">
      <p class="address">Address: 4817 Marlowe Blvd,<br>Suite B-100, Frisco, TX 75034</p>
      <p class="phone">Phone: (469) 555-0182</p>
      <p class="fax">Fax: (972) 555-0137</p>
    </section>

    <div class="location-tab tab-two">Location 2</div>
    <section class="details details-two">
      <p class="address">Address:&nbsp; 1936 Belvane Road,<br>Suite 100, Plano, TX 75075</p>
      <p class="phone">Phone: (469) 555-0169</p>
      <p class="fax">Fax: (972) 555-0137</p>
    </section>

    <svg class="brand-seal" viewBox="0 0 336 336" aria-label="Willow Brook">
      <circle cx="168" cy="168" r="158" fill="var(--paper)" stroke="var(--teal-deep)" stroke-width="18"/>
      <text class="brand-name" x="168" y="160" text-anchor="middle">Willow</text>
      <text class="brand-name" x="168" y="198" text-anchor="middle">Brook</text>
    </svg>
  </main>
</body>
</html>
```